Quillrests.com website overhaul

We want to upgrade our Wix website into a professional looking page for our growing business. The content that is online now needs to be used but the site should have a new look and feel from top to bottom. QuillRests is a company in the hospital and nursing home space. We would like to see the website use our color scheme but other than that we are open to any and all ideas. www.quillrests.com

```html
<!DOCTYPE html>
<html lang="en">
<head>
<meta charset="utf-8">
<title>QuillRests – Air Filtration for Healthcare</title>
<link href="https://fonts.googleapis.com/css2?family=Montserrat:wght@300;400;500;600;700;800&display=swap" rel="stylesheet">
<style>
:root{
  --brand:#5a63ad;
  --brand-dark:#4b539c;
  --ink:#2a1457;
  --body:#2b2b3a;
  --accent:#e4573b;
  --hero-top:#dfe4ec;
  --hero-bottom:#c9d3e2;
  --tint:#eef0fa;
  --white:#ffffff;
  --black:#000000;
}
*{box-sizing:border-box;margin:0;padding:0}
html,body{width:1200px;height:3374px;overflow:hidden}
body{position:relative;font-family:"Montserrat",sans-serif;color:var(--body);background:var(--white)}
.abs{position:absolute}
a{color:inherit;text-decoration:none}

/* header */
.site-header{position:absolute;left:0;top:0;width:1200px;height:84px;background:var(--brand)}
.brand{position:absolute;left:115px;top:18px;display:flex;align-items:center;gap:12px;color:var(--white);font-weight:600;font-size:34px}
.brand-mark{width:40px;height:40px;border-radius:50%;background:var(--white);opacity:.9}
.brand-rule{width:2px;height:48px;background:var(--white)}
.nav{position:absolute;top:33px;font-size:16px;color:var(--white);font-weight:500}
.nav.active{text-decoration:underline;font-weight:700}
.btn-contact{position:absolute;left:972px;top:22px;width:116px;height:41px;background:var(--white);color:var(--brand);border-radius:3px;font-weight:700;font-size:15px;display:flex;align-items:center;justify-content:center}

/* hero */
.hero{position:absolute;left:0;top:84px;width:1200px;height:676px;background:linear-gradient(var(--hero-top),var(--hero-bottom));clip-path:polygon(0 0,100% 0,100% 82%,50% 100%,0 81%)}
.hero-title{position:absolute;left:0;width:1200px;top:98px;text-align:center;font-size:53px;font-weight:700;color:var(--black)}
.btn{position:absolute;background:var(--brand);color:var(--white);font-weight:700;font-size:21px;display:flex;align-items:center;justify-content:center;border-radius:3px}

/* content */
.heading{position:absolute;font-weight:700;color:var(--ink);font-size:35px;line-height:43px;padding-left:16px;border-left:4px solid var(--brand)}
.copy{position:absolute;font-size:15px;line-height:26px;font-weight:400;color:var(--body)}
.copy p+p{margin-top:26px}
.frame{position:absolute;border:7px solid var(--accent);border-radius:3px}
.frame .art{width:100%;height:100%}
.tint-band{position:absolute;left:0;top:1350px;width:1200px;height:662px;background:var(--tint)}

/* info sheet */
.info{position:absolute;left:0;top:2556px;width:1200px;height:480px;background:var(--accent)}
.info-title{position:absolute;left:0;width:1200px;top:2620px;text-align:center;color:var(--white);font-size:36px;font-weight:700}
.info-title span{border-left:4px solid var(--white);padding-left:16px}
.info-copy{position:absolute;left:170px;width:860px;top:2680px;text-align:center;color:var(--white);font-size:15px;line-height:26px}

/* footer */
.footer-head{position:absolute;color:var(--white);font-size:22px;font-weight:500}
.footer-item{position:absolute;color:var(--white);font-size:15px}
.social{position:absolute;top:3182px;width:28px;height:28px;border-radius:50%;background:var(--accent)}
.newsletter-input{position:absolute;left:855px;top:3118px;width:233px;height:52px;background:var(--white);border-radius:2px;font-size:12px;color:#444;padding:19px 12px}
.newsletter-btn{position:absolute;left:855px;top:3188px;width:233px;height:50px;background:var(--accent);color:var(--white);font-size:18px;display:flex;align-items:center;justify-content:center;border-radius:2px}
.footer-rule{position:absolute;left:111px;top:3293px;width:977px;height:1px;background:#888}
.copyright{position:absolute;left:0;width:1200px;top:3326px;text-align:center;color:var(--white);font-size:11px}
</style>
</head>
<body>

<header class="site-header">
  <div class="brand"><span class="brand-mark"></span><span class="brand-rule"></span><span>QuillRests</span></div>
  <a class="nav active" style="left:604px">Home</a>
  <a class="nav" style="left:694px">How it Works</a>
  <a class="nav" style="left:842px">Resources</a>
  <a class="btn-contact">Contact Us</a>
</header>

<section class="hero" role="img" aria-label="Illustration of a hospital room with a patient bed and a QuillRests filtration unit circulating clean air"></section>
<svg class="abs" style="left:0;top:600px" width="1200" height="170" viewBox="0 0 1200 170">
  <polyline points="0,40 600,157 1200,40" fill="none" stroke="var(--accent)" stroke-width="5"/>
</svg>
<h1 class="hero-title">Welcome To QuillRests</h1>
<a class="btn" style="left:517px;top:173px;width:166px;height:64px">Get Started</a>

<!-- Section 1 -->
<h2 class="heading" style="left:111px;top:818px;width:520px">Greater Protection than an N95 Mask*</h2>
<div class="copy" style="left:111px;top:906px;width:480px">
  <p>According to the National Health Agency Study, "Expedient Methods for Surge Airborne Isolation within Healthcare Settings during Response to a Natural or Manmade Epidemic", the expedient airborne isolation research discussed within this document has identified isolation configurations that rely upon inexpe nsive, off-the-shelf materials &amp; HEPA filtration systems that are commonly found within healthcare facilities.</p>
  <p>Most provide better real-time source protection from infectious aerosol than that expected to result from an N95 respirator.</p>
</div>
<a class="btn" style="left:111px;top:1206px;width:167px;height:64px">Read More</a>
<div class="frame" style="left:642px;top:826px;width:446px;height:440px">
  <div class="art" role="img" aria-label="Illustration of layered HEPA filter panels capturing particles beside a hospital bed" style="background:linear-gradient(#b9c6d8,#8fa3c0 60%,#2f5fa5)"></div>
</div>

<!-- Section 2 -->
<div class="tint-band"></div>
<svg class="abs" style="left:0;top:1350px" width="540" height="662" viewBox="0 0 540 662">
  <polygon points="0,0 295,0 535,662 0,662" fill="var(--brand)"/>
</svg>
<div class="frame" style="left:112px;top:1442px;width:459px;height:488px">
  <div class="art" role="img" aria-label="Video still of an animated clinician beside a patient in bed, with a play button" style="background:linear-gradient(#1e9bc4,#1886b2 70%,#5a5f73)"></div>
</div>
<svg class="abs" style="left:295px;top:1645px" width="84" height="84" viewBox="0 0 84 84" aria-label="Play video">
  <circle cx="42" cy="42" r="40" fill="#e8334f"/>
  <polygon points="34,27 60,42 34,57" fill="#fff"/>
</svg>
<h2 class="heading" style="left:642px;top:1432px;width:540px">Enhanced Protection Against Airborne Infectious Particles</h2>
<div class="copy" style="left:642px;top:1570px;width:455px">
  <p>The QuillRests is an air filtration system that reduces the exposure to airborne infectious particles for healthcare workers, patients, and visitors by utilizing a source -focused technology that captures airborne infectious particles at the source.</p>
  <p>The QuillRests utilizes a patent-pending headboard design that pulls air from the head area of the patient through a HEPA filtration system and exhausts filtered air back into the room.</p>
</div>
<a class="btn" style="left:643px;top:1845px;width:168px;height:64px">Read More</a>

<!-- Section 3 -->
<h2 class="heading" style="left:113px;top:2123px;width:480px">Deploys in Minutes</h2>
<div class="copy" style="left:112px;top:2183px;width:490px">
  <p>The QuillRests is a complete system that can be deployed in a matter of minutes using only basic tools.</p>
  <p>The system easily disassembles for sanitation.In several cases, the protection is several times better.</p>
</div>
<div class="abs" style="left:112px;top:2322px;font-size:32px;font-weight:700;color:var(--ink)">9 Minutes</div>
<div class="copy" style="left:112px;top:2370px;width:490px;color:var(--black)">Turns over air in a 15 x 20 room in 9 minutes.</div>
<a class="btn" style="left:113px;top:2413px;width:167px;height:63px">Read More</a>
<div class="frame" style="left:643px;top:2094px;width:447px;height:382px">
  <div class="art" role="img" aria-label="Illustration of a hospital bed with air flowing from the headboard into the filtration unit" style="background:linear-gradient(#d3dbe6,#c6d0de 78%,#d9a98a)"></div>
</div>

<!-- Info sheet -->
<section class="info"></section>
<h2 class="info-title"><span>QuillRests PDF Quick Info Sheet</span></h2>
<p class="info-copy">Quick download for a printable information piece on the QuillRests system.The QuillRests utilizes a patent-pending headboard design that pulls air from the head area of the patient through a HEPA filtration system and exhausts filtered air back into the room.</p>
<a class="btn" style="left:374px;top:2784px;width:450px;height:64px;gap:22px">QuillRests PDF Quick Info Sheet
  <svg width="24" height="24" viewBox="0 0 24 24" fill="none" stroke="#fff" stroke-width="2.5"><path d="M12 3v12M6 10l6 6 6-6M3 20h18"/></svg>
</a>

<!-- Footer -->
<svg class="abs" style="left:0;top:2880px" width="1200" height="494" viewBox="0 0 1200 494">
  <polygon points="0,148 600,22 1200,148 1200,494 0,494" fill="var(--black)"/>
  <polyline points="0,134 600,12 1200,134" fill="none" stroke="var(--white)" stroke-width="5"/>
</svg>
<div class="brand" style="top:3090px;left:113px;font-size:28px"><span class="brand-mark" style="width:34px;height:34px"></span><span class="brand-rule" style="height:44px"></span><span>QuillRests</span></div>
<div class="footer-item" style="left:115px;top:3144px">Follow Us On:</div>
<span class="social" style="left:114px"></span>
<span class="social" style="left:162px"></span>
<span class="social" style="left:210px"></span>
<span class="social" style="left:258px"></span>

<div class="footer-head" style="left:382px;top:3066px">Quick Links</div>
<div class="footer-item" style="left:382px;top:3119px">›&nbsp; Home</div>
<div class="footer-item" style="left:382px;top:3154px">›&nbsp; About</div>
<div class="footer-item" style="left:382px;top:3189px">›&nbsp; Deploy</div>
<div class="footer-item" style="left:382px;top:3224px">›&nbsp; Contact Us</div>

<div class="footer-head" style="left:578px;top:3066px">Contact Us</div>
<div class="footer-item" style="left:578px;top:3119px">
  <svg width="14" height="14" viewBox="0 0 24 24" fill="none" stroke="#fff" stroke-width="2" style="vertical-align:-2px;margin-right:6px"><path d="M5 3h4l2 5-3 2a12 12 0 006 6l2-3 5 2v4a2 2 0 01-2 2A18 18 0 013 5a2 2 0 012-2z"/></svg>(302) 555-0147</div>
<div class="footer-item" style="left:578px;top:3159px;line-height:26px">
  <svg width="14" height="14" viewBox="0 0 24 24" fill="none" stroke="#fff" stroke-width="2" style="vertical-align:-2px;margin-right:6px"><path d="M12 22s7-7 7-12a7 7 0 00-14 0c0 5 7 12 7 12z"/><circle cx="12" cy="10" r="2.5"/></svg>QuillRests<br><span style="padding-left:22px">United States</span></div>
<div class="footer-item" style="left:578px;top:3219px">
  <svg width="14" height="14" viewBox="0 0 24 24" fill="none" stroke="#fff" stroke-width="2" style="vertical-align:-2px;margin-right:6px"><rect x="3" y="5" width="18" height="14"/><path d="M3 5l9 8 9-8"/></svg>hello@quillrests.com</div>

<div class="footer-head" style="left:854px;top:3066px">Sign Up Newsletter</div>
<div class="newsletter-input">Enter Email</div>
<div class="newsletter-btn">Submit</div>

<div class="footer-rule"></div>
<p class="copyright">Copyrights@2022.QuillRests.All Rights Reserved</p>

</body>
</html>
```